New high end server provider needs wordpress design

www.kv7hosting.com

Need a wordpress design for a high end server provider that provides overclocked dedicated servers for rent. We are located in Chicago but we have a presence is Virginia and Nevada for both our east and west coast customers.

We are a server provider that specializes in top end hardware with every feature designed for optimum performance. If it is not the best quality part or provides the best possible performance we don't run it. Our customers are mainly those that want the best single threaded performance possible from their hardware. We would be selling our services directly on our website via WHMCS.

We would like to see designs that are very modern and simplistic yet very attractive looking and catchy. Would prefer colors in the blues and greens and white. These colors are not necessary and I would be open to another color scheme if it looks good.

The final design should show speed and performance while being simplistic and easy on the eyes.

Logo and company name added and payment changed to guaranteed.  Looking for a wordpress template with the same pages as kv7hosting.com but with a redesigned look and feel.  

WHMCS control panel design also part of the design request.

If you have any questions please let me know!  This is just for kv7hosting.com and a main page for WHMCS (no coding just design).

Target Market(s)

IT Guru's (mostly men in their 20's to 30's)

Industry/Entity Type

Hardware

Requirements
Must have
• WHMCS panel design to fit with website theme.
Nice to have
• Main slider on home page similar to one of our other websites at www.kv7hosting.com
Should not have
• Flash or frames

```html
<!DOCTYPE html>
<html lang="en">
<head>
<meta charset="utf-8">
<title>KV7HOSTING – About</title>
<link href="https://fonts.googleapis.com/css2?family=Arimo:wght@400;700&family=Exo+2:wght@600&family=Oswald:wght@600&family=PT+Sans:wght@400;700&family=Lora&display=swap" rel="stylesheet">
<style>
:root{
  --green:#7ea812;
  --green-dark:#5e8a08;
  --navy:#1d3a73;
  --hero:#2f4f8f;
  --hero-dark:#203d77;
  --blue:#2a5fd4;
  --footer:#1c4fd0;
  --footer-dark:#1743b8;
  --ink:#2b2b2b;
  --muted:#666;
  --page:#eeeeee;
  --white:#ffffff;
}
*{box-sizing:border-box;margin:0;padding:0}
html,body{width:784px;height:1200px;overflow:hidden}
body{position:relative;background:var(--page);font-family:"Arimo",Arial,sans-serif;color:var(--muted)}
.abs{position:absolute}

/* header */
.site-header{left:0;top:0;width:784px;height:45px;background:var(--white)}
.brand{left:78px;top:10px;display:flex;align-items:center;gap:7px;font:700 19px "PT Sans",sans-serif;color:var(--navy);letter-spacing:.5px}
.brand i{width:18px;height:18px;border-radius:50%;background:var(--navy);display:block}
.main-nav{right:0;top:0;display:flex;height:45px}
.main-nav a{display:block;padding:0 14px;line-height:45px;font:600 12.5px "Exo 2",sans-serif;color:var(--green);text-decoration:none;letter-spacing:.5px}
.main-nav a.current{background:var(--green);color:var(--white);padding:0 12px}

/* hero */
.hero{left:0;top:45px;width:784px;height:295px;background:linear-gradient(180deg,var(--hero-dark),var(--hero) 55%,#35569a)}
.hero-title{left:78px;top:117px;width:372px;height:87px;background:rgba(255,255,255,.2);padding:9px 13px;font:600 25px/37px "Oswald",sans-serif;color:var(--white);text-transform:uppercase;letter-spacing:.3px}
.hero-points{left:78px;top:213px;width:259px}
.hero-points li{list-style:none;background:#d3d6de;border:1px solid #a9b0c2;margin-bottom:2px;height:15px;font-size:8.5px;line-height:14px;color:#333;padding-left:4px}
.hero-visual{left:478px;top:85px;width:202px;height:215px;background:linear-gradient(90deg,#3a3a3e,#1f1f22 60%,#4a4a50);border-radius:3px}
.arrow{top:182px;width:44px;height:44px;border-radius:50%;background:rgba(255,255,255,.18)}
.arrow.prev{left:23px}.arrow.next{left:716px}

/* content card */
.content-card{left:77px;top:340px;width:633px;height:623px;background:#f7f7f7;box-shadow:0 2px 6px rgba(0,0,0,.2)}
.welcome{left:0;top:0;width:633px;height:172px;background:var(--white)}
.welcome h1{left:20px;top:20px;font:400 31px/32px "PT Sans",sans-serif;color:var(--ink)}
.welcome .rule{left:181px;top:22px;width:1px;height:137px;background:#777}
.welcome .copy{left:193px;top:22px;width:420px;font-size:8.6px;line-height:13.2px;color:#555}
.welcome .copy p{margin-bottom:13px}
.section-title{left:0;top:195px;width:633px;text-align:center;font:400 29px "PT Sans",sans-serif;color:var(--ink)}

.package{background:var(--white);border:1px solid #e2e2e2;text-align:center}
.package h2{font:400 18.5px "PT Sans",sans-serif;color:var(--ink)}
.price{background:var(--blue);color:var(--white);font:400 29px "Lora",serif;height:50px;line-height:50px}
.price sup{font-size:10px;vertical-align:14px}
.price small{font-size:7px}
.price.text{font-size:16px}
.features{list-style:none;font-size:8.8px;line-height:18.6px;color:#555;margin-top:10px}
.btn{display:inline-block;width:76px;height:22px;line-height:20px;border-radius:2px;background:linear-gradient(var(--green),var(--green-dark));border:1px solid #4f7a05;color:var(--white);font:400 9.5px "PT Sans",sans-serif}
.pkg-basic{left:16px;top:257px;width:190px;height:326px}
.pkg-plus{left:206px;top:243px;width:218px;height:354px;box-shadow:0 2px 6px rgba(0,0,0,.22);z-index:2}
.pkg-custom{left:424px;top:257px;width:190px;height:326px}
.package h2{margin-top:10px;height:28px}
.pkg-plus h2{margin-top:10px;height:24px}

/* footer */
.site-footer{left:0;top:1009px;width:784px;height:161px;background:linear-gradient(var(--footer),var(--footer-dark))}
.col{top:25px;color:var(--white)}
.col h3{font:400 12.5px "PT Sans",sans-serif;margin-bottom:10px}
.col li{list-style:none;font-size:8px;line-height:16px}
.col li::before{content:"▪ ";font-size:6px}
.col p{font-size:8px;line-height:11px;margin-bottom:8px}
.col a{color:var(--white)}
.divider{top:15px;width:1px;height:135px;background:rgba(255,255,255,.25)}
.footer-brand{left:570px;top:61px;display:flex;align-items:center;gap:6px;font:700 17px "PT Sans",sans-serif;color:#0e2f86}
.footer-brand i{width:16px;height:16px;border-radius:50%;background:#0e2f86;display:block}
.legal{left:0;top:1170px;width:784px;height:30px;background:#e6e6e6;font-size:7.5px;color:#333;line-height:30px;padding:0 78px;display:flex;justify-content:space-between}
</style>
</head>
<body>
<header class="site-header abs">
  <div class="brand abs"><i></i>KV7HOSTING</div>
  <nav class="main-nav abs">
    <a href="#">HOME</a><a class="current" href="#">ABOUT</a><a href="#">PRODUCTS</a><a href="#">SERVICES</a><a href="#">NEWS</a><a href="#">CONTACT</a>
  </nav>
</header>

<section class="hero abs">
  <div class="arrow prev abs"><svg width="44" height="44"><path d="M26 13 L17 22 L26 31" stroke="#2f4f8f" stroke-width="4" fill="none"/></svg></div>
  <div class="arrow next abs"><svg width="44" height="44"><path d="M18 13 L27 22 L18 31" stroke="#2f4f8f" stroke-width="4" fill="none"/></svg></div>
  <div class="hero-visual abs" role="img" aria-label="Two rack server towers"></div>
</section>
<h2 class="hero-title abs">Speeds that set us<br>apart from the competition</h2>
<ul class="hero-points abs">
  <li>Lorem Ipsum is that it has a more-or-less normal.</li>
  <li>Distribution of letters, as opposed to using 'Content here.</li>
  <li>Lorem Ipsum making it look like readable English.</li>
</ul>

<main class="content-card abs">
  <section class="welcome abs">
    <h1 class="abs">welcome to<br>kv7hosting</h1>
    <div class="rule abs"></div>
    <div class="copy abs">
      <p>KV7Hosting offer the highest quality, highest performing Frontline Siege 2 servers available for rent. Our servers are custom built specifically for the demanding requirements of Frontline Siege 2 Beta. Each Frontline Siege 2 game server is ran on a 4.4 Ghz overclocked quad core Q4 4400x CPU, so you can be assured that our servers will be able to run at high tickrates with 20+ players.</p>
      <p>Unlike most game server providers, we offer unlimited player slots on all of our rentals. This means that you can increase the player count when the game becomes more optimized, ensuring that your server will always be one of the most popular and best performing Frontline Siege 2 servers around.</p>
      <p>Interested in ordering? See our Pricing Page for more information.</p>
    </div>
  </section>
  <h2 class="section-title abs">Dedicated Servers</h2>

  <article class="package pkg-basic abs">
    <h2>Basic Package</h2>
    <div class="price"><sup>$</sup>160 <small>/Month</small></div>
    <ul class="features"><li>Quad core Q4 4400x 4.4 Ghz CPU</li><li>8 GB DDR3 1600 Ram</li><li>320 GB Hard Drive</li><li>4 IP addresses</li><li>1,500 GB monthly Bandwidth</li><li>(3) FS2 servers pre-configured</li><li>(1) Website hosting</li><li>Remote Desktop Access</li></ul>
    <div style="margin-top:12px"><span class="btn">Contact Us</span></div>
  </article>
  <article class="package pkg-plus abs">
    <h2>Plus Package</h2>
    <div class="price"><sup>$</sup>185 <small>/Month</small></div>
    <ul class="features"><li>Quad core Q4 4400x 4.4 Ghz CPU</li><li>8 GB DDR3 1600 Ram</li><li>320 GB Hard Drive</li><li>4 IP addresses</li><li>1,500 GB monthly Bandwidth</li><li>(3) FS2 servers pre-configured</li><li>(1) Website hosting</li><li>Remote Desktop Access</li></ul>
    <div style="margin-top:12px"><span class="btn">Contact Us</span></div>
  </article>
  <article class="package pkg-custom abs">
    <h2>Custom Package</h2>
    <div class="price text">Varies / Month</div>
    <ul class="features"><li>Quad core Q4 4400x 4.4 Ghz CPU</li><li>8 GB DDR3 1600 Ram</li><li>320 GB Hard Drive</li><li>4 IP addresses</li><li>1,500 GB monthly Bandwidth</li><li>(3) FS2 servers pre-configured</li><li>(1) Website hosting</li><li>Remote Desktop Access</li></ul>
    <div style="margin-top:12px"><span class="btn">Contact Us</span></div>
  </article>
</main>

<footer class="site-footer abs">
  <div class="col abs" style="left:75px">
    <h3>Kv7hosting</h3>
    <ul><li>Home</li><li>About Us</li><li>Our Services</li><li>Our Products</li><li>Contact Us</li><li>Latest News</li></ul>
  </div>
  <div class="divider abs" style="left:174px"></div>
  <div class="col abs" style="left:196px">
    <h3>Contact to kv7hosting</h3>
    <p>48 Harbor Lane<br>Westfield, Northern Territory 5090</p>
    <p>+61 (0) 8 5550 1234</p>
    <p>+61 (0) 8 5550 5678</p>
    <p>info@kv7hosting.com</p>
  </div>
  <div class="divider abs" style="left:343px"></div>
  <div class="col abs" style="left:363px;width:180px">
    <h3>Latest News Updates</h3>
    <p>Lorem ipsum dolor sit amet conse ctetuer adipiscing elit. Aenean dolor.<br>August 3, 2012 &nbsp;|&nbsp; <a href="#">Read More</a></p>
    <p>Lorem ipsum dolor sit amet conse ctetuer adipiscing elit. Aenean dolor.<br>August 3, 2012 &nbsp;|&nbsp; <a href="#">Read More</a></p>
  </div>
  <div class="divider abs" style="left:559px"></div>
  <div class="footer-brand abs"><i></i>KV7HOSTING</div>
</footer>
<div class="legal abs"><span>All Right Resereved Copyright © 2012 - Privacy Policy - Terms of Use</span><span>Powered By Brightgrid Studio</span></div>
</body>
</html>
```